The Harbor Keys Method self-help book

Create a front cover, back cover and spine for a book.
Make a profile of a runner crossing the finish line, bursting a red ribbon. Make the word Harbor red as well.

Industry/Entity Type

Psychology

Colors

Designer to choose colors to be used in the design.

Requirements
Must have
• see images uploaded

```html
<!DOCTYPE html>
<html lang="en">
<head>
<meta charset="utf-8">
<title>The Harbor Keys Method — Book Cover</title>
<link rel="stylesheet" href="https://fonts.googleapis.com/css2?family=Montserrat:wght@500;600;700;800&display=swap">
<style>
  :root {
    --cover-red: #e8262a;
    --band-slate: #3e5a72;
    --text-white: #ffffff;
    --sky-top: #7f9c99;
    --sky-mid: #c9d6cf;
    --sun-core: #fff8e6;
    --sun-warm: #f2b35a;
    --foliage-dark: #3c3f36;
    --ground-dark: #2f2e2b;
  }
  html, body {
    margin: 0;
    padding: 0;
    width: 800px;
    height: 1200px;
    overflow: hidden;
    background: #ffffff;
  }
  .cover {
    position: relative;
    width: 800px;
    height: 1200px;
    overflow: hidden;
    font-family: "Montserrat", "Helvetica Neue", Arial, sans-serif;
  }
  .cover-photo {
    position: absolute;
    inset: 0;
    background:
      radial-gradient(circle at 500px 650px, var(--sun-core) 0, rgba(255,240,210,0.95) 70px, rgba(242,179,90,0.55) 190px, rgba(242,179,90,0) 380px),
      radial-gradient(ellipse 260px 600px at 60px 560px, rgba(60,63,54,0.85) 0, rgba(60,63,54,0) 100%),
      linear-gradient(to bottom, var(--sky-top) 0%, var(--sky-mid) 35%, #e9ebdf 52%, #a9a595 64%, #6f6b62 76%, var(--ground-dark) 100%);
  }
  .author-name {
    position: absolute;
    top: 40px;
    left: 0;
    width: 800px;
    margin: 0;
    text-align: center;
    color: var(--text-white);
    font-weight: 600;
    font-size: 44px;
    letter-spacing: 0.5em;
    text-indent: 0.5em;
    line-height: 1;
  }
  .book-title {
    margin: 0;
    font-size: inherit;
  }
  .title-band {
    position: absolute;
    left: 48px;
    margin: 0;
    padding: 0 26px;
    background: var(--cover-red);
    color: var(--text-white);
    font-weight: 700;
    font-size: 74px;
    line-height: 80px;
    letter-spacing: -0.01em;
    white-space: nowrap;
  }
  .title-band--the { top: 861px; }
  .title-band--middle { top: 949px; right: 0; }
  .title-band--last { top: 1040px; }
  .genre-band {
    position: absolute;
    left: 48px;
    top: 1132px;
    width: 324px;
    height: 48px;
    box-sizing: border-box;
    padding-left: 26px;
    background: var(--band-slate);
    color: var(--text-white);
    font-weight: 700;
    font-size: 27px;
    line-height: 48px;
    margin: 0;
    white-space: nowrap;
  }
</style>
</head>
<body>
  <main class="cover">
    <div class="cover-photo" role="img" aria-label="Photograph: low-angle view of a woman running along a dirt trail into a bright setting sun, trees on the left and a checkered finish flag"></div>
    <p class="author-name">MARTIN CALDER</p>
    <h1 class="book-title">
      <span class="title-band title-band--the">THE</span>
      <span class="title-band title-band--middle">HARBOR KEYS</span>
      <span class="title-band title-band--last">METHOD</span>
    </h1>
    <p class="genre-band">SELF-HELP BOOK</p>
  </main>
</body>
</html>
```